Book Cover for Collection of Dark Short Stories

I need a cover design for my book "Amber Harbors." It will be a 5 x 8 paperback roughly 200 pages long. There will be 11 short stories in it of a darker nature. The book is a mixture of science fiction, historical fiction, and just interesting to read stories. The stories focus on individuals or people facing difficult situations such as terrifying end of the world scenarios, mortal danger in wars, as well as crushing debt and a job layoff.
I envision the cover with dark colors (blue/black). One suggestion is to have the silhouette of a man outside sitting on a log or hill with him looking slightly down in contemplation. There are dark clouds covering most of the sky, but the stars and/or moon are trying to shine through in one small area. There's a small amount of hope in the gloom.
I see the mood of the cover as darkly reflective.

I will be happy to look at other suggestions, too.

I will also have some text on the back with a small author photo in the middle. I see the back cover as a continuation of the front cover with dark clouds and again the small amount of light from the moon and stars.
I don't want any violence or death in the cover.
I'll be happy to look at suggestions for the back cover area from the designers.
Updates

The title of the book is: AMBER HARBORS a subtitle in a smaller font somewhere below should read: A Collection of Short Stories My name should be at the bottom of the cover: Dale Marbury

Hey designers, Please find the text for the back cover here: This fascinating collection of short stories is a unique blend of science fiction, action, and historical fiction that will entertain and challenge you. In Amber Harbors’ 11 intriguing stories, we experience one isolated man’s survival as he holds out and awaits the terrifying arrival of otherworldly visitors; firsthand battlefield accounts with some strange occurrences in both WW II and the Revolutionary War; and a tiger hunt in India that goes very wrong. We also see tales of modern woe revolving around some of life’s common miseries, accompanied by brave and unexpected measures to fight against them. In addition, we witness an awkward and dangerous stay in an underground bunker with an unstable host; two astronauts stranded on a lifeless asteroid who only have one old-fashioned form of entertainment; an eerie post-plague world dominated by an unlikely species; and an eccentric astronaut orbiting the Earth who is happiest on his own, except for one furry exception. Dale Marbury’s interesting stories travel in different directions, but spring from one deep source: the darker side of the imagination. I also have an author photo that I would like either below the text or in between, whichever looks better. Feel free to crop it without my hands or whatever looks best.

Target Market(s)

Men 18-65, but crossover appeal to women is fine, too.

Font styles to use
Serif

Colors
0255a3
000000
1b1b1b
dcdcdc
fbf289

Requirements
Must have
• AMBER HARBORS in some form.
Nice to have
• Some interesting takes on AMBER HARBORS and the silhouette of a man sitting and contemplating deep things (like the end of the world).
Should not have
• No violence, sex, death, or anything provocative in the cover. I want to convey a serious, dark contemplative mood with a slight amount of hope.

```html
<!DOCTYPE html>
<html lang="en">
<head>
<meta charset="utf-8">
<title>Amber Harbors — Cover Spread</title>
<link rel="stylesheet" href="https://fonts.googleapis.com/css2?family=Montserrat:wght@300;400;500;700&family=Cinzel:wght@400;500&display=swap">
<style>
  :root {
    --page-bg: #ffffff;
    --night: #050708;
    --night-deep: #000000;
    --teal-glow: #3f6f78;
    --sky-blue: #5f8fb0;
    --cloud-grey: #1b1b1b;
    --text-light: #ffffff;
    --text-soft: #dcdcdc;
    --photo-warm: #8a6a55;
    --photo-suit: #2a3246;
  }
  html, body {
    margin: 0;
    padding: 0;
    width: 960px;
    height: 1200px;
    overflow: hidden;
    background: var(--page-bg);
  }
  .canvas {
    position: relative;
    width: 960px;
    height: 1200px;
  }
  .spread {
    position: absolute;
    left: 0;
    top: 251px;
    width: 960px;
    height: 698px;
    overflow: hidden;
    background: var(--night);
    color: var(--text-light);
    font-family: "Montserrat", sans-serif;
  }
  .spread-art {
    position: absolute;
    inset: 0;
    background:
      radial-gradient(circle at 918px 96px, rgba(230,240,245,0.95) 0 20px, rgba(150,190,210,0.55) 22px, rgba(0,0,0,0) 60px),
      radial-gradient(ellipse 260px 170px at 780px 210px, rgba(95,143,176,0.55), rgba(0,0,0,0) 70%),
      radial-gradient(ellipse 340px 200px at 660px 380px, rgba(63,111,120,0.55), rgba(0,0,0,0) 70%),
      radial-gradient(ellipse 400px 220px at 260px 230px, rgba(40,70,70,0.45), rgba(0,0,0,0) 70%),
      radial-gradient(ellipse 520px 120px at 640px 560px, rgba(40,60,70,0.45), rgba(0,0,0,0) 70%),
      linear-gradient(180deg, #0b1112 0%, #081012 55%, #030404 100%);
  }
  .back-title {
    position: absolute;
    left: 30px;
    top: 113px;
    width: 380px;
    margin: 0;
    text-align: center;
    font-weight: 700;
    font-size: 37px;
    letter-spacing: 0.3px;
    line-height: 1;
  }
  .back-subtitle {
    position: absolute;
    left: 30px;
    top: 166px;
    width: 380px;
    text-align: center;
    font-weight: 400;
    font-size: 16px;
    color: var(--text-soft);
  }
  .back-author {
    position: absolute;
    left: 30px;
    top: 198px;
    width: 380px;
    text-align: center;
    font-family: "Cinzel", serif;
    font-size: 22px;
    letter-spacing: 0.5px;
  }
  .author-photo {
    position: absolute;
    left: 46px;
    top: 259px;
    width: 119px;
    height: 169px;
    background: linear-gradient(180deg, #6c6a5a 0%, var(--photo-warm) 45%, var(--photo-suit) 75%, #1c2030 100%);
  }
  .blurb {
    position: absolute;
    margin: 0;
    text-align: justify;
    font-weight: 500;
  }
  .blurb-side {
    left: 174px;
    top: 258px;
    width: 224px;
    font-size: 9.6px;
    line-height: 14.6px;
  }
  .blurb-side p { margin: 0 0 11px; }
  .blurb-main {
    left: 42px;
    top: 444px;
    width: 356px;
    font-size: 10.6px;
    line-height: 16.1px;
  }
  .spine-title {
    position: absolute;
    left: 510px;
    top: 123px;
    transform-origin: 0 0;
    transform: rotate(90deg);
    white-space: nowrap;
    font-weight: 700;
    font-size: 37px;
    line-height: 1;
    margin: 0;
  }
  .spine-subtitle {
    position: absolute;
    left: 466px;
    top: 193px;
    transform-origin: 0 0;
    transform: rotate(90deg);
    white-space: nowrap;
    font-weight: 400;
    font-size: 14px;
    line-height: 1;
    color: var(--text-soft);
  }
  .spine-author {
    position: absolute;
    left: 420px;
    top: 636px;
    width: 120px;
    text-align: center;
    font-family: "Cinzel", serif;
    font-size: 13.5px;
    line-height: 16px;
  }
  .front-title {
    position: absolute;
    left: 560px;
    top: 304px;
    width: 370px;
    margin: 0;
    text-align: center;
    font-weight: 700;
    font-size: 68px;
    line-height: 1.02;
    letter-spacing: -0.5px;
  }
  .front-subtitle {
    position: absolute;
    left: 560px;
    top: 469px;
    width: 370px;
    text-align: center;
    font-weight: 400;
    font-size: 21px;
  }
  .front-author {
    position: absolute;
    left: 560px;
    top: 642px;
    width: 370px;
    text-align: center;
    font-family: "Cinzel", serif;
    font-size: 23px;
    letter-spacing: 0.6px;
  }
</style>
</head>
<body>
<div class="canvas">
  <section class="spread">
    <div class="spread-art" role="img" aria-label="Dark cloudy night sky with a glowing full moon at upper right and the silhouette of a man bent forward in contemplation over a dim shoreline"></div>

    <div class="back-cover">
      <h2 class="back-title">AMBER HARBORS</h2>
      <div class="back-subtitle">A Collection of Short Stories</div>
      <div class="back-author">DALE MARBURY</div>
      <div class="author-photo" role="img" aria-label="Author portrait photo"></div>
      <div class="blurb blurb-side">
        <p>This fascinating collection of short stories is a unique blend of science fiction, action, and historical fiction that will entertain and challenge you.</p>
        <p>In Amber Harbors’ 11 intriguing stories, we experience one isolated man’s survival as he holds out and awaits the terrifying arrival of otherworldly visitors; firsthand battlefield accounts with some strange occurrences in both WW II and the Revolutionary War; and a tiger hunt in India that goes very wrong.</p>
      </div>
      <p class="blurb blurb-main">We also see tales of modern woe revolving around some of life’s common miseries, accompanied by brave and unexpected measures to fight against them. In addition, we witness an awkward and dangerous stay in an underground bunker with an unstable host; two astronauts stranded on a lifeless asteroid who only have one old-fashioned form of entertainment; an eerie post-plague world dominated by an unlikely species; and an eccentric astronaut orbiting the Earth who is happiest on his own, except for one furry exception. Dale Marbury’s interesting stories travel in different directions, but spring from one deep source: the darker side of the imagination.</p>
    </div>

    <div class="spine">
      <h2 class="spine-title">AMBER HARBORS</h2>
      <div class="spine-subtitle">A Collection of Short Stories</div>
      <div class="spine-author">DALE<br>MARBURY</div>
    </div>

    <div class="front-cover">
      <h1 class="front-title">AMBER<br>HARBORS</h1>
      <div class="front-subtitle">A Collection of Short Stories</div>
      <div class="front-author">DALE MARBURY</div>
    </div>
  </section>
</div>
</body>
</html>
```